Web Design job - Condo Debts Collection Business needs a Web Design

I need a site for a client, who works with condo debts collection, and ensure all revenues provided by condo fees will be always available to the building manager of condo on a specific date, regardless of defaults.
I have the visual identity (logo, slogan and colors) of the company, and some requirements on layout (kind of slider, menu options, phone number on a noble position, etc) - maybe I can do a sketch, but I like the idea of give some freedom to designer.

*** PLEASE, we have no interest in templates. We want something new***

Target Market(s)

I have two targets for this design: - Condominium's building manager. This target is looking for a solution to overdue debts on it's condo. - Residents on condominiums. This target wants to live in a better place, where their neighbors pay their condominium fees on time.

Number of Pages Required

1 page

Requirements
Must have
• - Slider with title, some short text related, a nice image (I prefer happy and/or peaceful family, people doing business, happy friends, and so on).
• - I have a special attention to menu. I'm looking for one I can have a nice effect, more elegant, charming, kind of innovative.
• - Phone number on the top (or clearly visible).
• - Member log in area or icon on the top (or clearly visible).
• - News/articles area.
• - Modern fonts, with good quality, sans-serif on areas where reading is more intensive (prefer Google web-fonts).
• - Colors specified on attached files.
Nice to have
• - Clear background color, cause it's better to read larger texts (like articles). Dark backgrounds makes reading difficult.
• - A site with effects (like shadows, lines, curves, gradients, lights) is usually pretty.
• - I pay attention on beautiful footers.
Should not have
• - Images with a lot of money (I don't sell richness, I sell tranquility, peace, harmony, safety).
• - Poor menu.

```html
<!DOCTYPE html>
<html lang="en">
<head>
<meta charset="utf-8">
<title>Velora – Condo Debts Collection</title>
<link rel="stylesheet" href="https://fonts.googleapis.com/css2?family=Alegreya+Sans:wght@300;400;500;700;800&family=Merriweather+Sans:wght@700;800&family=Lato:wght@400;700&display=swap">
<style>
:root{
  --orange:#e3a01b;
  --yellow:#e6c02c;
  --bronze:#b08a33;
  --ink:#222;
  --text:#666;
  --muted:#888;
  --light:#f5f5f5;
  --cream:#fbf6e8;
  --footer:#231f1e;
  --white:#fff;
}
*{margin:0;padding:0;box-sizing:border-box}
html,body{width:1200px;height:2675px;overflow:hidden}
body{position:relative;background:var(--white);font-family:"Alegreya Sans",sans-serif;color:var(--text)}
.abs{position:absolute}

/* header */
.brand{position:absolute;left:100px;top:24px;display:flex;align-items:center;gap:12px}
.brand-mark{width:54px;height:54px;background:var(--yellow)}
.brand-name{font-family:"Alegreya Sans",sans-serif;font-weight:800;font-size:56px;line-height:46px;color:#2b2b2b;letter-spacing:1px}
.brand-tag{font-size:12px;font-weight:700;color:#2b2b2b;letter-spacing:.5px;margin-top:4px}
.call{position:absolute;left:638px;top:14px;display:flex;align-items:center;gap:8px;font-size:23px;color:#444}
.call b{font-weight:700;color:#222}
.member{position:absolute;left:936px;top:14px;width:162px;height:38px;border:2px solid var(--orange);border-radius:20px;color:var(--orange);font-family:Lato,sans-serif;font-size:13px;font-weight:700;text-align:center;line-height:34px}
.nav{position:absolute;left:484px;top:62px;width:616px;height:44px;background:var(--orange);border-radius:12px 12px 0 0;display:flex;justify-content:space-around;align-items:center;padding:0 10px;font-family:Lato,sans-serif;font-size:13px;font-weight:700;color:var(--white);z-index:3}
.nav .active{position:relative}
.nav .active::after{content:"";position:absolute;left:50%;top:29px;margin-left:-8px;border:8px solid transparent;border-top-color:var(--orange)}

/* hero */
.hero{position:absolute;left:0;top:105px;width:1200px;height:600px;background:linear-gradient(180deg,#7e8c9c 0%,#4e5a6c 45%,#2a3140 100%)}
.hero-title{position:absolute;left:0;width:1200px;top:286px;text-align:center;font-family:"Merriweather Sans",sans-serif;font-weight:800;font-size:63px;line-height:70px;color:var(--white);letter-spacing:.5px}
.hero-sub{position:absolute;left:0;width:1200px;top:358px;text-align:center;font-size:21px;font-weight:700;color:var(--white)}
.btn-solid{position:absolute;left:506px;top:403px;width:188px;height:46px;background:var(--orange);border-radius:23px;color:var(--white);font-family:Lato,sans-serif;font-size:18px;letter-spacing:1px;text-align:center;line-height:46px}
.hero-curve{position:absolute;left:0;top:640px}

/* sections */
.pattern{background:linear-gradient(180deg,#fdfaf1 0%,var(--cream) 50%,#fdfaf1 100%)}
.welcome{position:absolute;left:0;top:700px;width:1200px;height:410px}
.services{position:absolute;left:0;top:1110px;width:1200px;height:595px;background:var(--light)}
.articles{position:absolute;left:0;top:1705px;width:1200px;height:640px}
.heading{position:absolute;left:0;width:1200px;text-align:center;font-weight:700;font-size:34px;color:var(--ink)}
.rule{position:absolute;left:564px;width:72px;height:3px;background:var(--orange)}
.intro{position:absolute;left:170px;width:860px;text-align:center;font-size:15px;line-height:27px;color:var(--text)}
.btn-line{position:absolute;left:513px;width:174px;height:44px;border:2px solid var(--orange);border-radius:22px;color:var(--orange);font-size:19px;font-weight:500;display:flex;align-items:center;justify-content:center;gap:10px;background:var(--white)}

.card{position:absolute;top:1296px;width:302px;height:302px;background:var(--white);box-shadow:0 2px 6px rgba(0,0,0,.08);text-align:center}
.card-icon{width:104px;height:104px;border-radius:50%;margin:36px auto 0;display:flex;align-items:center;justify-content:center}
.card h3{margin-top:20px;font-weight:400;font-size:25px;color:var(--ink)}
.card p{margin:14px auto 0;width:230px;font-size:15px;line-height:22px;color:var(--text)}

.post{position:absolute;top:1860px;width:310px;height:245px}
.post-photo{position:absolute;inset:0;clip-path:polygon(0 0,100% 0,100% 97%,0 100%)}
.post-text{position:absolute;left:17px;right:17px;bottom:38px;color:var(--white)}
.post-text h4{font-weight:700;font-size:18px;line-height:20px;text-transform:uppercase}
.post-text time{display:block;margin-top:12px;font-size:11px}
.read{display:flex;align-items:center;gap:6px;margin-top:14px;color:var(--orange);font-size:14px;font-weight:500}

/* footer */
.footer{position:absolute;left:0;top:2275px;width:1200px;height:400px}
.foot-brand{position:absolute;left:100px;top:2392px;display:flex;align-items:center;gap:12px;color:var(--white)}
.foot-brand .brand-name,.foot-brand .brand-tag{color:var(--white)}
.foot-brand .brand-mark{background:var(--white)}
.foot-about{position:absolute;left:100px;top:2488px;width:260px;font-size:10px;line-height:15px;color:#aaa}
.foot-col{position:absolute;top:2403px;color:var(--white)}
.foot-col h5{font-size:19px;font-weight:700;margin-bottom:14px}
.foot-col li{list-style:none;font-size:13px;line-height:30px;color:#ddd;display:flex;align-items:center;gap:6px}
.dot{width:8px;height:8px;border-radius:50%;background:#ddd;display:inline-block}
.foot-rule{position:absolute;left:100px;top:2598px;width:1000px;height:1px;background:#3a3534}
.copy{position:absolute;left:100px;top:2623px;font-size:11px;color:#ccc}
.legal{position:absolute;left:948px;top:2624px;font-size:9px;color:#888;display:flex;gap:22px}
</style>
</head>
<body>

<header>
  <div class="brand">
    <div class="brand-mark"></div>
    <div>
      <div class="brand-name">velora</div>
      <div class="brand-tag">COBRANÇA CONDOMINIAL</div>
    </div>
  </div>
  <div class="call">
    <svg width="32" height="32" viewBox="0 0 32 32"><circle cx="16" cy="16" r="14.5" fill="none" stroke="var(--orange)" stroke-width="2"/><path d="M11 9c1-1 2-1 3 0l1.5 2.5c.5 1 0 1.7-.8 2.3 1 2 2.3 3.4 4.3 4.3.6-.8 1.3-1.3 2.3-.8L23.8 19c1 1 1 2 0 3-1.5 1.6-4 1.8-7-.5-3-2.3-5.5-5.5-6.2-8-.6-2 .1-3.5.4-4.5z" fill="var(--orange)"/></svg>
    <span>Call Us: <b>(55) 4100.2763</b></span>
  </div>
  <div class="member">MEMBER LOGIN</div>
  <nav class="nav">
    <span class="active">HOME</span><span>ABOUT US</span><span>OUR SERVICES</span><span>BLOG</span><span>CONTACT US</span>
  </nav>
</header>

<section class="hero" role="img" aria-label="Business people meeting in a bright office with city view">
</section>
<div class="hero-title">CONDO DEBTS COLLECTION</div>
<div class="hero-sub">Quis autem vel eum iure reprehenderit qui in ea voluptate velit esse quam nihil molestiae consequatur</div>
<div class="btn-solid">CONTACT US</div>
<svg class="abs" style="left:42px;top:352px" width="20" height="40" viewBox="0 0 20 40"><path d="M16 2 4 20l12 18" fill="none" stroke="#fff" stroke-opacity=".7" stroke-width="2"/></svg>
<svg class="abs" style="left:1138px;top:352px" width="20" height="40" viewBox="0 0 20 40"><path d="M4 2l12 18L4 38" fill="none" stroke="#fff" stroke-opacity=".7" stroke-width="2"/></svg>

<section class="welcome pattern"></section>
<svg class="hero-curve" width="1200" height="64" viewBox="0 0 1200 64"><path d="M0 58Q600 -40 1200 58V64H0z" fill="#fdfaf1"/></svg>
<h2 class="heading" style="top:726px">WELCOME TO VELORA</h2>
<div class="rule" style="top:771px"></div>
<p class="intro" style="top:795px">Lorem ipsum dolor sit amet, consectetur adipiscing elit, sed do eiusmod tempor incididunt ut labore et dolore magna aliqua. Ut enim ad minim veniam, quis nostrud exercitation ullamco laboris nisi ut aliquip ex ea commodo consequat. Duis aute irure dolor in reprehenderit in voluptate velit esse cillum dolore eu fugiat nulla pariatur.</p>
<p class="intro" style="top:904px">Sed ut perspiciatis unde omnis iste natus error sit voluptatem accusantium doloremque laudantium, totam rem aperiam, eaque ipsa quae ab illo inventore veritatis et quasi architecto beatae vitae dicta sunt explicabo.</p>
<div class="btn-line" style="top:991px">Learn more <svg width="26" height="10" viewBox="0 0 26 10"><path d="M0 5h24M19 1l5 4-5 4" fill="none" stroke="var(--orange)" stroke-width="1.5"/></svg></div>

<section class="services"></section>
<h2 class="heading" style="top:1178px">OUR SERVICES</h2>
<div class="rule" style="top:1231px"></div>

<div class="card" style="left:102px">
  <div class="card-icon" style="background:var(--orange)">
    <svg width="54" height="54" viewBox="0 0 54 54"><rect x="20" y="6" width="18" height="26" rx="2" fill="#fff" transform="rotate(15 29 19)"/><rect x="8" y="22" width="34" height="22" rx="4" fill="#fff"/><rect x="32" y="29" width="12" height="8" rx="2" fill="var(--orange)"/></svg>
  </div>
  <h3>DEBT COLLECTION</h3>
  <p>Reiciendis voluptatibus maiores alias consequatur aut perferendis.</p>
</div>
<div class="card" style="left:449px">
  <div class="card-icon" style="background:var(--yellow)">
    <svg width="54" height="54" viewBox="0 0 54 54"><rect x="12" y="6" width="26" height="36" rx="2" fill="none" stroke="#fff" stroke-width="3"/><path d="M18 16h14M18 22h14M18 28h8" stroke="#fff" stroke-width="3"/><circle cx="38" cy="38" r="9" fill="#fff"/><path d="M34 38l3 3 5-6" fill="none" stroke="var(--yellow)" stroke-width="2.5"/></svg>
  </div>
  <h3>INVOICE CHECKING</h3>
  <p>Reiciendis voluptatibus maiores alias consequatur aut perferendis.</p>
</div>
<div class="card" style="left:797px">
  <div class="card-icon" style="background:var(--bronze)">
    <svg width="60" height="54" viewBox="0 0 60 54"><circle cx="30" cy="14" r="6" fill="#fff"/><circle cx="14" cy="20" r="5" fill="#fff"/><circle cx="46" cy="20" r="5" fill="#fff"/><path d="M20 34a10 10 0 0 1 20 0z M5 38a9 9 0 0 1 18 0z M37 38a9 9 0 0 1 18 0z" fill="#fff"/><rect x="6" y="40" width="48" height="6" rx="3" fill="#fff"/></svg>
  </div>
  <h3>INSOLVENCY SERVICES</h3>
  <p>Reiciendis voluptatibus maiores alias consequatur aut perferendis.</p>
</div>

<section class="articles pattern"></section>
<h2 class="heading" style="top:1755px">LATEST ARTICLES</h2>
<div class="rule" style="top:1810px"></div>

<article class="post" style="left:100px">
  <div class="post-photo" role="img" aria-label="Black and white photo of a smiling family outdoors" style="background:linear-gradient(160deg,#8a8a8a,#3a3a3a)"></div>
  <div class="post-text"><h4>Dolore magnam aliquam quaerat voluptatem</h4><time>APRIL 14, 2015</time></div>
</article>
<article class="post" style="left:444px">
  <div class="post-photo" role="img" aria-label="Dark photo of paperwork on a desk" style="background:linear-gradient(160deg,#4a4a4a,#1e1e1e)"></div>
  <div class="post-text" style="bottom:58px"><h4>Sed quia non numquam eius modi tempora</h4><time>JANUARY 20, 2015</time>
    <div class="read">READ MORE <svg width="14" height="14" viewBox="0 0 14 14"><circle cx="7" cy="7" r="7" fill="var(--orange)"/><path d="M4 7h6M7 4l3 3-3 3" fill="none" stroke="#222" stroke-width="1.5"/></svg></div>
  </div>
</article>
<article class="post" style="left:790px">
  <div class="post-photo" role="img" aria-label="Black and white photo of a couple relaxing on a lawn in front of a house" style="background:linear-gradient(160deg,#9a9a9a,#404040)"></div>
  <div class="post-text"><h4>Nostrum exercitationem ullam corporis suscipit</h4><time>APRIL 14, 2015</time></div>
</article>

<div class="btn-line" style="top:2160px">View more <svg width="26" height="10" viewBox="0 0 26 10"><path d="M0 5h24M19 1l5 4-5 4" fill="none" stroke="var(--orange)" stroke-width="1.5"/></svg></div>

<footer>
  <svg class="footer" width="1200" height="400" viewBox="0 0 1200 400"><path d="M0 60L1200 4V400H0z" fill="var(--footer)"/></svg>
  <div class="foot-brand">
    <div class="brand-mark"></div>
    <div>
      <div class="brand-name">velora</div>
      <div class="brand-tag">COBRANÇA CONDOMINIAL</div>
    </div>
  </div>
  <p class="foot-about">At vero eos et accusamus et iusto odio dignissimos ducimus qui blanditiis praesentium voluptatum deleniti atque.</p>
  <div class="foot-col" style="left:535px"><h5>Quick Links</h5><ul><li>Home</li><li>About Us</li><li>Our Services</li><li>Blog</li></ul></div>
  <div class="foot-col" style="left:775px"><h5>Information</h5><ul><li>Our Partners</li><li>Team</li><li>Client Login</li><li>Contact Us</li></ul></div>
  <div class="foot-col" style="left:1011px"><h5>Help Center</h5><ul><li><span class="dot"></span>Gatherly</li><li><span class="dot"></span>Murmur</li><li><span class="dot"></span>Reelcast</li><li><span class="dot"></span>Moodwall</li></ul></div>
  <div class="foot-rule"></div>
  <div class="copy">© 2018 VELORA. All right reserved.</div>
  <div class="legal"><span>Terms &amp; Condition</span><span>Privacy Policy</span></div>
</footer>

</body>
</html>
```